Commercial construction contractor website.

We need a website that contains About Us, Contact info, Services, Project pictures and Industry News section

Target Market(s)

I'm building industral/flex spaces/commercial.

Industry/Entity Type

Commercial/industrial construction

Coding

Coded - Design and coding required

Number of Pages Required

5+ page

Font styles to use
Other font styles liked:
• The logo font is Microgramma Pro

Requirements
Must have
• Must have correct company name spelling: Dunmore Ridge Construction
Nice to have
• I do like to see our logo design implemented in the design
Should not have
• Please do not show big city pictures and business suit people. We are a commercial construction company

```html
<!DOCTYPE html>
<html lang="en">
<head>
<meta charset="utf-8">
<title>Dunmore Ridge Construction</title>
<link rel="stylesheet" href="https://fonts.googleapis.com/css2?family=Montserrat:wght@400;500;600;700&display=swap">
<style>
:root{
  --black:#000;
  --bar:#1c2027;
  --nav:#20252e;
  --panel:#22262d;
  --blue:#0a4fb0;
  --label:#1d5ec4;
  --orange:#f07d00;
  --white:#fff;
  --muted:#8a8f98;
  --soft:#c9ccd2;
}
*{margin:0;padding:0;box-sizing:border-box}
html,body{width:1200px;height:4551px;overflow:hidden;background:var(--black)}
body{font-family:"Montserrat",sans-serif;color:var(--white)}
.page{position:relative;width:1200px;height:4551px;overflow:hidden;background:var(--black)}
.abs{position:absolute}
.topbar{left:0;top:0;width:1200px;height:28px;background:var(--bar);font-size:8px;color:var(--soft)}
.topbar .item{position:absolute;top:9px;display:flex;align-items:center;gap:6px}
.topbar svg{width:9px;height:9px;fill:var(--soft)}
.social{display:flex;gap:18px}
.social span{display:block;width:7px;height:7px;border-radius:50%;background:var(--soft)}
.nav{left:0;top:28px;width:1200px;height:66px;background:var(--nav);border-bottom:1px solid #2c313b}
.brand{position:absolute;display:flex;flex-direction:column;align-items:center;font-weight:600;color:var(--white);text-transform:uppercase;text-align:center}
.brand .dot{border-radius:50%;background:var(--blue)}
.nav .brand{left:292px;top:14px;width:76px;font-size:5px;letter-spacing:.3px;gap:4px}
.nav .brand .dot{width:18px;height:18px}
.menu{position:absolute;top:29px;font-size:7.5px;font-weight:500;text-transform:uppercase;color:var(--soft);letter-spacing:.3px}
.talk{left:830px;top:48px;width:98px;height:28px;background:var(--blue);font-size:8px;font-weight:700;text-transform:uppercase;display:flex;align-items:center;justify-content:center;border-radius:2px}
.hero{left:0;top:94px;width:1200px;height:516px;background:linear-gradient(90deg,#3b3a37 0%,#5d4f44 28%,#8a7c6e 55%,#9b8f82 80%,#7a7067 100%)}
.hero-title{left:562px;top:228px;font-size:34px;font-weight:700;line-height:1.2}
.hero-text{left:562px;top:336px;width:320px;font-size:12px;line-height:2}
.btn-orange{left:562px;top:431px;width:159px;height:34px;background:var(--orange);font-size:10px;font-weight:500;display:flex;align-items:center;justify-content:center}
.label{font-size:7px;font-weight:600;letter-spacing:1.4px;text-transform:uppercase;color:var(--label)}
.h2{font-size:20px;font-weight:700;line-height:1.55}
.body{font-size:10px;line-height:1.9;color:var(--muted)}
.more{font-size:9px;font-weight:700}
.photo{border-radius:0}
.card{left:613px;width:297px;background:var(--panel);border-radius:2px}
.card .chev{position:absolute;left:22px;width:26px;height:26px;border-radius:50%;display:flex;align-items:center;justify-content:center}
.card .chev svg{width:8px;height:8px;stroke-width:2;fill:none}
.card .title{position:absolute;left:60px;font-size:10px;font-weight:600}
.circle-btn{width:32px;height:32px;border-radius:50%;background:var(--blue);display:flex;align-items:center;justify-content:center}
.circle-btn svg{width:9px;height:9px;fill:var(--white)}
.tile{top:1744px;height:438px}
.tile .cat{position:absolute;left:27px;font-size:7px;font-weight:700;letter-spacing:1.2px;text-transform:uppercase}
.tile .name{position:absolute;left:27px;font-size:13px;font-weight:600;line-height:1.65;width:220px}
.seeall{left:562px;top:2239px;width:85px;height:28px;background:#2a2f38;font-size:8px;font-weight:600;display:flex;align-items:center;justify-content:center}
.partner{display:flex;align-items:center;gap:10px;color:#5b6069}
.partner .sq{width:24px;height:24px;background:#3d424b}
.partner small{display:block;font-size:7px;font-weight:400;line-height:1}
.partner b{display:block;font-size:17px;font-weight:700;text-transform:uppercase;line-height:1.1}
.quote{left:300px;top:3160px;width:600px;text-align:center;font-size:17px;line-height:1.9;color:var(--muted)}
.quote strong{color:var(--soft);font-weight:500}
.news-img{top:3525px;width:302px;height:196px}
.news-date{top:3741px;font-size:8px;font-weight:600;letter-spacing:1px;color:var(--soft)}
.news-title{top:3772px;font-size:13px;font-weight:600;line-height:1.6}
.cta{left:295px;top:3905px;width:618px;height:154px;background:var(--panel)}
.cta p{position:absolute;left:62px;top:62px;font-size:12.5px;line-height:1.9;color:var(--soft)}
.cta .quote-btn{position:absolute;left:454px;top:64px;width:104px;height:30px;background:var(--blue);font-size:8px;font-weight:600;display:flex;align-items:center;justify-content:center}
.footer{left:0;top:4158px;width:1200px;height:393px;background:var(--panel)}
.footer .brand{left:283px;top:85px;width:98px;font-size:7px;gap:6px}
.footer .brand .dot{width:28px;height:28px}
.footer h4{position:absolute;font-size:9px;font-weight:700}
.footer .link{position:absolute;font-size:8.5px;color:var(--muted)}
.footer .about{left:283px;top:176px;width:180px;font-size:8.5px;line-height:1.95;color:var(--muted)}
.totop{left:896px;top:4471px;width:28px;height:28px;border-radius:50%;background:var(--blue);display:flex;align-items:center;justify-content:center}
.totop svg{width:8px;height:8px;fill:none;stroke:var(--white);stroke-width:2}
</style>
</head>
<body>
<div class="page">

  <header>
    <div class="abs topbar">
      <div class="item" style="left:283px"><svg viewBox="0 0 10 10"><path d="M2 0l2 2-1 1.5c.6 1.3 1.9 2.6 3.5 3.5L8 6l2 2-1.5 2C4 9.5.5 6 0 1.5z"/></svg>+1 555 014 2290</div>
      <div class="item" style="left:366px"><svg viewBox="0 0 10 10"><path d="M0 2h10v6H0zM0 2l5 3.5L10 2" fill="none" stroke="#c9ccd2"/></svg>support@dunmoreridgeconstruction.com</div>
      <div class="item" style="left:555px"><svg viewBox="0 0 10 10"><path d="M5 0a3.5 3.5 0 0 1 3.5 3.5C8.5 6 5 10 5 10S1.5 6 1.5 3.5A3.5 3.5 0 0 1 5 0z"/></svg>Mon - Sat: 8:00am - 18:00pm</div>
      <div class="item social" style="left:845px"><span></span><span></span><span></span><span></span></div>
    </div>
    <nav class="abs nav">
      <div class="brand"><span class="dot"></span>Dunmore Ridge Construction</div>
      <span class="menu" style="left:413px">Home</span>
      <span class="menu" style="left:459px">About us</span>
      <span class="menu" style="left:521px">Projects</span>
      <span class="menu" style="left:583px">Services</span>
      <span class="menu" style="left:641px">Industry news</span>
      <span class="menu" style="left:726px">Contact</span>
    </nav>
    <a class="abs talk">Talk to us</a>
  </header>

  <section>
    <div class="abs hero" role="img" aria-label="Smiling site worker in hard hat and safety vest beside a concrete wall, colleagues in the background"></div>
    <h1 class="abs hero-title">We build everything<br>with passion</h1>
    <p class="abs hero-text">You want to know how we work and take a tour of one of our works!</p>
    <a class="abs btn-orange">Come for a tour</a>
  </section>

  <section>
    <p class="abs label" style="left:304px;top:763px">About us</p>
    <h2 class="abs h2" style="left:304px;top:784px">Leaders in construction<br>and ready to work</h2>
    <p class="abs body" style="left:304px;top:870px;width:260px">With more than 15,000 employees and in constant growth we are ready to build your personal or commercial project.</p>
    <a class="abs more" style="left:304px;top:958px">Know more</a>
    <div class="abs photo" style="left:613px;top:712px;width:292px;height:308px;background:linear-gradient(135deg,#f4a84a,#e98d2c 60%,#d97a1e)" role="img" aria-label="Work glove covered in plaster dust against an orange background"></div>
  </section>

  <section>
    <div class="abs" style="left:288px;top:1117px;width:262px;height:415px;background:radial-gradient(ellipse at 55% 45%,rgba(232,170,40,.35),rgba(80,80,90,.15) 55%,transparent 75%)" role="img" aria-label="Network-line illustration of a head wearing a hard hat"></div>
    <h2 class="abs h2" style="left:613px;top:1131px;font-size:19px">What we do</h2>
    <div class="abs card" style="top:1212px;height:131px">
      <span class="chev" style="top:24px;background:var(--blue)"><svg viewBox="0 0 8 8" stroke="#fff"><path d="M3 1l3 3-3 3"/></svg></span>
      <span class="title" style="top:30px">Construction building</span>
      <p class="body" style="position:absolute;left:72px;top:52px;width:205px;font-size:9px">We build everything you annex, from family houses to mega-exports of great power, we are ready</p>
    </div>
    <div class="abs card" style="top:1359px;height:71px">
      <span class="chev" style="top:22px;background:#f0dfc0"><svg viewBox="0 0 8 8" stroke="#22262d"><path d="M3 1l3 3-3 3"/></svg></span>
      <span class="title" style="top:30px;color:var(--soft)">Advanced planning</span>
    </div>
    <div class="abs card" style="top:1447px;height:71px">
      <span class="chev" style="top:22px;background:#f0dfc0"><svg viewBox="0 0 8 8" stroke="#22262d"><path d="M3 1l3 3-3 3"/></svg></span>
      <span class="title" style="top:30px;color:var(--soft)">Interior architecture</span>
    </div>
  </section>

  <section>
    <p class="abs label" style="left:295px;top:1631px">Gallery</p>
    <h2 class="abs h2" style="left:295px;top:1650px;font-size:19px">See our final work</h2>
    <a class="abs circle-btn" style="left:1048px;top:1648px"><svg viewBox="0 0 8 8"><path d="M6 0L1 4l5 4z"/></svg></a>
    <a class="abs circle-btn" style="left:1087px;top:1648px"><svg viewBox="0 0 8 8"><path d="M2 0l5 4-5 4z"/></svg></a>

    <div class="abs tile" style="left:90px;width:343px;background:linear-gradient(180deg,#5fa4b6 0%,#6b7d80 45%,#3a322c 100%)" role="img" aria-label="Tall stone tower seen from below against a blue sky">
      <span class="cat" style="top:352px">Building</span>
      <span class="name" style="top:372px">Art deco skyscraper in the center</span>
    </div>
    <div class="abs tile" style="left:435px;width:342px;background:linear-gradient(180deg,#c99b86 0%,#b48471 55%,#4a3d39 100%)" role="img" aria-label="High-rise tower at dusk under a pink sky">
      <span class="cat" style="top:352px">Building</span>
      <span class="name" style="top:372px">Second tallest building in Boston</span>
    </div>
    <div class="abs tile" style="left:781px;width:339px;background:linear-gradient(180deg,#6fb3c4 0%,#7fa6ae 35%,#3c4346 65%,#5d8990 100%)" role="img" aria-label="Cantilevered modern house with a flat roof against the sky">
      <span class="cat" style="top:306px">Architecture</span>
      <span class="name" style="top:326px">Modern and minimalist house</span>
      <span class="more" style="position:absolute;left:27px;top:406px;font-size:8px">Read More &nbsp;→</span>
    </div>
    <a class="abs seeall">See All</a>
  </section>

  <section>
    <p class="abs label" style="left:295px;top:2450px">How we work</p>
    <h2 class="abs h2" style="left:295px;top:2468px">See how we work with<br>our clients</h2>
    <p class="abs body" style="left:295px;top:2557px;width:255px">This is how we start each job we carry out, always complying with a series of protocols, both safety and health.</p>
    <a class="abs more" style="left:295px;top:2645px">Know more</a>
    <div class="abs" style="left:610px;top:2368px;width:484px;height:369px;background:linear-gradient(135deg,#d9d9d9 0%,#cfb8a0 40%,#c9835a 70%,#b66f4a 100%)" role="img" aria-label="Overhead view of workers in hard hats reviewing plans on a dusty site"></div>
    <a class="abs circle-btn" style="left:578px;top:2520px;width:46px;height:46px"><svg viewBox="0 0 8 8"><path d="M2 0l6 4-6 4z"/></svg></a>
  </section>

  <section>
    <div class="abs partner" style="left:302px;top:2848px"><span class="sq"></span><div><small>Arch</small><b>Kestrel</b></div></div>
    <div class="abs partner" style="left:540px;top:2848px"><span class="sq"></span><div><small>Lather</small><b>Bramwell</b></div></div>
    <div class="abs partner" style="left:778px;top:2848px"><span class="sq"></span><div><small>Studio</small><b>Orvane</b></div></div>
    <div class="abs partner" style="left:302px;top:2955px"><span class="sq"></span><div><small>Architecture</small><b>Tallis</b></div></div>
    <div class="abs partner" style="left:550px;top:2955px"><span class="sq"></span><div><small>Montreal</small><b>Corvid</b></div></div>
    <div class="abs partner" style="left:798px;top:2955px"><span class="sq"></span><div><small>Building</small><b>Hartfield</b></div></div>
  </section>

  <section>
    <p class="abs label" style="left:0;width:1200px;text-align:center;top:3095px">Testimonials</p>
    <p class="abs quote">We have recently built <strong>a complex of 4 apartments in a very short period of time,</strong> we are happy with your services</p>
    <a class="abs circle-btn" style="left:395px;top:3283px;width:44px;height:44px"><svg viewBox="0 0 8 8"><path d="M6 0L1 4l5 4z"/></svg></a>
    <a class="abs circle-btn" style="left:770px;top:3283px;width:44px;height:44px"><svg viewBox="0 0 8 8"><path d="M2 0l5 4-5 4z"/></svg></a>
    <div class="abs" style="left:536px;top:3283px;width:44px;height:44px;border-radius:50%;background:linear-gradient(135deg,#d9b8a0,#8a6a55)" role="img" aria-label="Client portrait"></div>
    <span class="abs" style="left:592px;top:3299px;font-size:9px;font-weight:600">Marta Quillon</span>
  </section>

  <section>
    <p class="abs label" style="left:295px;top:3425px">Blog</p>
    <h2 class="abs h2" style="left:295px;top:3444px;font-size:19px">Recent News</h2>
    <div class="abs news-img" style="left:295px;background:linear-gradient(135deg,#e2c45a,#c9c2b5 45%,#9a8f86)" role="img" aria-label="Workers in hard hats looking over building plans"></div>
    <div class="abs news-img" style="left:613px;background:radial-gradient(circle at 55% 70%,#f29a2a,#7a4418 35%,#2d2a28 75%)" role="img" aria-label="Angle grinder throwing sparks in a workshop"></div>
    <p class="abs news-date" style="left:295px">October 5, 2020, 7:24 am</p>
    <p class="abs news-date" style="left:613px">October 5, 2020, 7:23 am</p>
    <h3 class="abs news-title" style="left:295px">Documentation needed<br>to start building</h3>
    <h3 class="abs news-title" style="left:613px">Machinery preferred for<br>construction by us</h3>
  </section>

  <section class="abs cta">
    <p>Request a quote for a completely free work, in<br>addition to professional advice.</p>
    <a class="quote-btn">Free quote</a>
  </section>

  <footer class="abs footer">
    <div class="brand"><span class="dot"></span>Dunmore Ridge Construction</div>
    <p class="abs about">At Dunmore Ridge Construction we care about each client and each person who works with us and makes great projects possible</p>
    <div class="abs social" style="left:283px;top:265px"><span></span><span></span><span></span></div>
    <h4 style="left:500px;top:86px">Who we are</h4>
    <span class="link" style="left:500px;top:120px">About Us</span>
    <span class="link" style="left:500px;top:148px">Our Team</span>
    <span class="link" style="left:500px;top:175px">Projects</span>
    <span class="link" style="left:500px;top:203px">Services</span>
    <h4 style="left:719px;top:86px">Contact Us</h4>
    <span class="link" style="left:719px;top:120px">Phone: +1 555 014 2290</span>
    <span class="link" style="left:719px;top:150px">Email: support@dunmoreridgeconstruction.com</span>
    <span class="link" style="left:719px;top:180px;width:210px;line-height:1.8">Address: 48 Foundry Lane, Dunmore Ridge, USA</span>
  </footer>
  <a class="abs totop"><svg viewBox="0 0 8 8"><path d="M1 5.5l3-3 3 3"/></svg></a>

</div>
</body>
</html>
```